Need simple and modern looking business card with all my information on one side and logo on the other side
Info :
Company name - VELMAR CONSTRUCTION LLC
Company addres- 418 harbor 87th. Dunmoor park ny 10352
Email- velmarllc@tridomail.Com
Company phone number 555-318-6094
Cell number- 555-742-0583
Web site - velmarllc.Com
My name Gerald tomasino

Target Market(s)

Construction , home improvement, remodeling

Industry/Entity Type

Construction

Contact Information for Business Card

It has to be moder but at the same time simple

Font styles to use
Sans Serif

Colors
0255a3
ffffff
000000
f78f20
b1b1b1
9d9d9d
1b1b1b
33a6d7
ec1f27

Requirements
Must have
• My logo on one side maybe with a some kind of background on the other side all my information
Nice to have
• Some kind of background pictures provided by you .PLEASE HAVE ACCOUNT WITH PIXELVAULT WILL NOT PAY ANY EXTRA FEES .
Should not have
• Any kind of hamer, nails,screws, helmets itp. Please do not copy the other designs come up with something new.

```html
<!DOCTYPE html>
<html lang="en">
<head>
<meta charset="utf-8">
<title>Velmar Construction LLC – Business Card</title>
<link rel="stylesheet" href="https://fonts.googleapis.com/css2?family=Roboto:wght@400;700&display=swap">
<style>
  :root {
    --blue: #0255a3;
    --white: #ffffff;
    --black: #000000;
    --orange: #f78f20;
    --grey-light: #b1b1b1;
    --grey-mid: #9d9d9d;
    --charcoal: #1b1b1b;
    --sky: #33a6d7;
    --red: #ec1f27;
    --stage: #454545;
    --card: #0b0b0b;
  }
  * { margin: 0; padding: 0; box-sizing: border-box; }
  html, body {
    width: 1200px; height: 950px; overflow: hidden;
    background: var(--stage);
    font-family: "Roboto", Arial, sans-serif;
  }
  .canvas { position: relative; width: 1200px; height: 950px; }

  .card {
    position: absolute;
    width: 620px; height: 354px;
    background: linear-gradient(160deg, var(--charcoal) 0%, var(--card) 55%, var(--black) 100%);
    border-radius: 4px;
    box-shadow: 0 18px 40px rgba(0,0,0,.45);
    color: var(--white);
    overflow: hidden;
  }
  .card--front { left: 190px; top: 70px; }
  .card--back  { left: 390px; top: 510px; }

  /* company name block */
  .wordmark {
    display: flex; align-items: center; gap: 14px;
    font-weight: 700; color: var(--white); text-transform: uppercase;
  }
  .wordmark__square { width: 16px; height: 16px; background: var(--orange); flex: none; }
  .wordmark__text { display: flex; flex-direction: column; line-height: 1; }
  .wordmark__name { font-size: 56px; letter-spacing: 4px; }
  .wordmark__sub  { font-size: 17px; letter-spacing: 3.2px; margin-top: 6px; }

  .card--front .wordmark {
    position: absolute; left: 50%; top: 50%;
    transform: translate(-50%, -50%);
  }

  .card--back .wordmark {
    position: absolute; right: 42px; top: 92px;
  }
  .card--back .wordmark__name { font-size: 42px; letter-spacing: 3px; }
  .card--back .wordmark__sub  { font-size: 13px; letter-spacing: 2.3px; }

  .address {
    position: absolute; right: 42px; top: 190px;
    font-size: 15px; line-height: 1.55; text-align: right;
    color: var(--white);
  }

  .person { position: absolute; left: 42px; top: 92px; }
  .person__name { font-size: 20px; font-weight: 700; color: var(--orange); }
  .person__role { font-size: 13px; font-weight: 700; margin-top: 8px; }

  .contacts {
    position: absolute; left: 42px; bottom: 34px;
    list-style: none; font-size: 14px; line-height: 1;
  }
  .contacts li { display: flex; align-items: center; gap: 10px; margin-top: 9px; }
  .contacts svg { width: 14px; height: 14px; flex: none; fill: var(--white); }
</style>
</head>
<body>
<main class="canvas">

  <section class="card card--front" aria-label="Business card front">
    <div class="wordmark">
      <span class="wordmark__square"></span>
      <span class="wordmark__text">
        <span class="wordmark__name">Velmar</span>
        <span class="wordmark__sub">Construction LLC</span>
      </span>
    </div>
  </section>

  <section class="card card--back" aria-label="Business card back">
    <div class="person">
      <p class="person__name">Gerald tomasino</p>
      <p class="person__role">CEO/Founder</p>
    </div>

    <ul class="contacts">
      <li>
        <svg viewBox="0 0 24 24" aria-hidden="true"><path d="M6.6 10.8a15.1 15.1 0 0 0 6.6 6.6l2.2-2.2a1 1 0 0 1 1-.25 11.4 11.4 0 0 0 3.6.6 1 1 0 0 1 1 1V20a1 1 0 0 1-1 1A17 17 0 0 1 3 4a1 1 0 0 1 1-1h3.5a1 1 0 0 1 1 1c0 1.25.2 2.45.6 3.6a1 1 0 0 1-.25 1z"/></svg>
        555-318-6094
      </li>
      <li>
        <svg viewBox="0 0 24 24" aria-hidden="true"><path d="M7 1h10a2 2 0 0 1 2 2v18a2 2 0 0 1-2 2H7a2 2 0 0 1-2-2V3a2 2 0 0 1 2-2zm0 3v14h10V4zm5 15.5a1 1 0 1 0 0 2 1 1 0 0 0 0-2z"/></svg>
        555-742-0583
      </li>
      <li>
        <svg viewBox="0 0 24 24" aria-hidden="true"><path d="M2 5h20v14H2zm2 2v.4l8 5 8-5V7zm0 2.8V17h16V9.8l-8 5z"/></svg>
        velmarllc@tridomail.Com
      </li>
      <li>
        <svg viewBox="0 0 24 24" aria-hidden="true"><path d="M12 2a10 10 0 1 0 0 20 10 10 0 0 0 0-20zm6.9 6h-3a15.6 15.6 0 0 0-1.3-3.6A8 8 0 0 1 18.9 8zM12 4c.8 1.2 1.5 2.5 1.9 4h-3.8c.4-1.5 1.1-2.8 1.9-4zM4.3 14a8 8 0 0 1 0-4h3.4a16 16 0 0 0 0 4zm.8 2h3a15.6 15.6 0 0 0 1.3 3.6A8 8 0 0 1 5.1 16zm3-8h-3a8 8 0 0 1 4.3-3.6A15.6 15.6 0 0 0 8.1 8zM12 20c-.8-1.2-1.5-2.5-1.9-4h3.8c-.4 1.5-1.1 2.8-1.9 4zm2.3-6H9.7a14 14 0 0 1 0-4h4.6a14 14 0 0 1 0 4zm.3 5.6a15.6 15.6 0 0 0 1.3-3.6h3a8 8 0 0 1-4.3 3.6zm1.7-5.6a16 16 0 0 0 0-4h3.4a8 8 0 0 1 0 4z"/></svg>
        velmarllc.Com
      </li>
    </ul>

    <div class="wordmark">
      <span class="wordmark__square"></span>
      <span class="wordmark__text">
        <span class="wordmark__name">Velmar</span>
        <span class="wordmark__sub">Construction LLC</span>
      </span>
    </div>

    <address class="address" style="font-style:normal">
      418 harbor 87th.<br>
      Dunmoor park ny 10352
    </address>
  </section>

</main>
</body>
</html>
```